Pelkman Agency (http://pa.quorvexstudio.com/)

We are looking for a similar design to what we have, but more professional looking and cleaned up with links and logo that is not so grainy looking. We are an independent insurance agency marketing to personal and commercial clients. We offer all commercial lines markets and all personal lines. We target excavators, landscapers, restaurants, golf courses, contractors. Please look at http://pa.quorvexstudio.com/ which we had designed but do not like it, it will give you an idea of what we are looking for.

Target Market(s)

Commercial and personal insurance. All business products and all personal (homeowners, auto, antique auto, umbrella)

Industry/Entity Type

It Professional

Logo Text

Knowledge Building Your Assurance

Number of Pages Required

5+ page

Colors
000000
848484
0255a3

```html
<!DOCTYPE html>
<html lang="en">
<head>
<meta charset="utf-8">
<title>Personal Insurance – Pelkman Agency</title>
<link rel="stylesheet" href="https://fonts.googleapis.com/css2?family=Roboto+Condensed:wght@300;400;700&display=swap">
<style>
:root{
  --brand-blue:#0255a3;
  --button-blue:#0d6efd;
  --ink:#000000;
  --text-grey:#848484;
  --body-grey:#6b6b6b;
  --panel:#efefef;
  --white:#ffffff;
  --line:#cfcfcf;
  --nav-mark:#9fbde0;
}
*{box-sizing:border-box;margin:0;padding:0}
html,body{width:852px;height:1200px;overflow:hidden}
body{position:relative;background:var(--white);font-family:"Roboto Condensed",Arial,sans-serif;color:var(--ink)}

.top-nav{position:absolute;left:0;top:0;width:852px;height:56px;background:var(--brand-blue);display:flex;align-items:center;padding-left:46px}
.top-nav a{color:var(--white);text-decoration:none;font-size:9.5px;font-weight:700;letter-spacing:.4px;text-transform:uppercase;white-space:nowrap}
.top-nav .sep{width:14px;height:12px;margin:0 10px;flex:none}

.site-header{position:absolute;left:0;top:56px;width:852px;height:74px;background:var(--white)}
.brand{position:absolute;left:46px;top:14px;display:flex;align-items:center;gap:10px}
.brand-dot{width:34px;height:44px;background:var(--brand-blue);border-radius:50%;flex:none}
.brand-name{display:block;font-size:23px;font-weight:400;color:var(--brand-blue);line-height:26px}
.brand-tagline{display:block;font-size:9px;font-weight:400;color:var(--text-grey);letter-spacing:.6px;text-transform:uppercase;line-height:13px}
.contact{position:absolute;top:14px;display:flex;gap:10px}
.contact svg{margin-top:3px;flex:none}
.contact-label{font-size:11px;color:var(--body-grey);line-height:14px}
.contact-value{font-size:10px;color:var(--text-grey);line-height:14px;white-space:nowrap}
.contact-phone{left:514px}
.contact-location{left:692px}

.content{position:absolute;left:0;top:130px;width:852px;height:886px;background:var(--panel)}
.page-title{position:absolute;left:0;top:37px;width:852px;text-align:center;font-size:28px;font-weight:400;letter-spacing:.3px}
.product{position:absolute;left:45px;width:780px;height:154px}
.product-photo{position:absolute;left:0;top:0;width:202px;height:154px}
.product-body{position:absolute;left:272px;top:-1px;width:340px}
.product-title{font-size:12px;font-weight:400;text-transform:uppercase;margin-bottom:3px;line-height:15px}
.product-text{font-size:10px;line-height:14.5px;color:var(--body-grey)}
.btn{position:absolute;left:272px;width:88px;height:30px;background:var(--button-blue);color:var(--white);font-size:10px;font-weight:400;text-transform:uppercase;display:flex;align-items:center;justify-content:center;text-decoration:none}

.newsletter{position:absolute;left:0;top:1016px;width:852px;height:184px;background:var(--white)}
.newsletter-title{position:absolute;left:55px;top:53px;font-size:29px;font-weight:300;color:#555}
.email-field{position:absolute;left:237px;top:56px;width:374px;height:33px;border:1px solid var(--line);font-size:8px;color:var(--text-grey);padding-left:10px;display:flex;align-items:center;text-transform:uppercase}
.subscribe{position:absolute;left:631px;top:56px;width:173px;height:33px;background:var(--text-grey);color:var(--white);font-size:13px;display:flex;align-items:center;justify-content:center;text-transform:uppercase}
.social{position:absolute;left:0;top:121px;width:852px;display:flex;justify-content:center;gap:10px}
.social span{width:12px;height:12px;border-radius:50%;background:var(--brand-blue)}
.copyright{position:absolute;left:0;top:153px;width:852px;text-align:center;font-size:9px;color:#c4c4c4;text-transform:uppercase}
.copyright b{font-weight:400;color:var(--brand-blue)}
</style>
</head>
<body>

<nav class="top-nav">
  <a href="#">Home</a>
  <svg class="sep" viewBox="0 0 14 12"><path d="M1 11L13 1M5 11L13 4.5" stroke="var(--nav-mark)" stroke-width="1"/></svg>
  <a href="#">Personal Insurance</a>
  <svg class="sep" viewBox="0 0 14 12"><path d="M1 11L13 1M5 11L13 4.5" stroke="var(--nav-mark)" stroke-width="1"/></svg>
  <a href="#">Business Insurance</a>
  <svg class="sep" viewBox="0 0 14 12"><path d="M1 11L13 1M5 11L13 4.5" stroke="var(--nav-mark)" stroke-width="1"/></svg>
  <a href="#">Service Center</a>
  <svg class="sep" viewBox="0 0 14 12"><path d="M1 11L13 1M5 11L13 4.5" stroke="var(--nav-mark)" stroke-width="1"/></svg>
  <a href="#">About Us</a>
  <svg class="sep" viewBox="0 0 14 12"><path d="M1 11L13 1M5 11L13 4.5" stroke="var(--nav-mark)" stroke-width="1"/></svg>
  <a href="#">Contact</a>
</nav>

<header class="site-header">
  <div class="brand">
    <span class="brand-dot"></span>
    <div>
      <span class="brand-name">Pelkman Agency</span>
      <span class="brand-tagline">Knowledge Building Your Assurance</span>
    </div>
  </div>
  <div class="contact contact-phone">
    <svg width="18" height="18" viewBox="0 0 24 24"><path fill="#0255a3" d="M6.6 10.8a15.1 15.1 0 0 0 6.6 6.6l2.2-2.2c.3-.3.7-.4 1-.2 1.1.4 2.3.6 3.6.6.6 0 1 .4 1 1V20c0 .6-.4 1-1 1A17 17 0 0 1 3 4c0-.6.4-1 1-1h3.5c.6 0 1 .4 1 1 0 1.3.2 2.5.6 3.6.1.3 0 .7-.2 1l-2.3 2.2z"/></svg>
    <div><div class="contact-label">Call Us Today:</div><div class="contact-value">1-888-4 PELKMAN</div></div>
  </div>
  <div class="contact contact-location">
    <svg width="16" height="22" viewBox="0 0 16 22"><path fill="#0255a3" d="M8 0a8 8 0 0 0-8 8c0 6 8 14 8 14s8-8 8-14a8 8 0 0 0-8-8zm0 11a3 3 0 1 1 0-6 3 3 0 0 1 0 6z"/></svg>
    <div><div class="contact-label">Location:</div><div class="contact-value">Birch Hollow, NJ 08899<br>Cedar Landing, NJ 08097</div></div>
  </div>
</header>

<main class="content">
  <h1 class="page-title">PERSONAL INSURANCE</h1>

  <section class="product" style="top:101px">
    <div class="product-photo" role="img" aria-label="Older couple at a laptop" style="background:linear-gradient(135deg,#e9e6e0,#cfc8bd 55%,#f3f1ee)"></div>
    <div class="product-body">
      <h2 class="product-title">Annuity Insurance</h2>
      <p class="product-text">Annuities may be a smart fit for your investment plan. An annuity is a long-term investment issued by an insurance company, designed to help protect you from the risk of outliving your income. Through annuitization, your purchase payments (what you contribute) are converted into periodic payments that can last for life.</p>
    </div>
    <a class="btn" href="#" style="top:113px">Click Here</a>
  </section>

  <section class="product" style="top:293px">
    <div class="product-photo" role="img" aria-label="Couple in a car" style="background:linear-gradient(135deg,#3a3a36,#8a7b6a 50%,#d8d2c8)"></div>
    <div class="product-body">
      <h2 class="product-title">Car Insurance</h2>
      <p class="product-text">Smart auto protection for you. Pelkman car insurance gives you quality protection at a great price. Every policy comes with the support of a knowledgeable and friendly Pelkman agent. With personal attention and service, you'll have the information you need to choose the coverage that makes the most sense for you.</p>
    </div>
    <a class="btn" href="#" style="top:98px">Click Here</a>
  </section>

  <section class="product" style="top:486px">
    <div class="product-photo" role="img" aria-label="Multi-generation family sitting on grass" style="background:linear-gradient(180deg,#8a9a5a,#c9b9a4 45%,#7a9a3a)"></div>
    <div class="product-body">
      <h2 class="product-title">Life Insurance</h2>
      <p class="product-text">Life insurance can help provide for the people who depend on you financially if you can't be there for them. The money can be used for final expenses, to replace lost income, cover debts, pay your mortgage, fund a child's education, and more.</p>
    </div>
    <a class="btn" href="#" style="top:99px">Click Here</a>
  </section>

  <section class="product" style="top:678px">
    <div class="product-photo" role="img" aria-label="Hands sheltering a seedling growing from coins" style="background:radial-gradient(ellipse at 50% 70%,#c9a879 0,#e8e0cf 35%,#f7f7f4 70%)"></div>
    <div class="product-body">
      <h2 class="product-title">Long Term Care Insurance</h2>
      <p class="product-text">Individuals who require long-term care are generally not sick in the traditional sense, but are unable to perform the basic activities of daily living (ADLs) such as dressing, bathing, eating, toileting, continence, transferring (getting in and out of a bed or chair), and walking.</p>
    </div>
    <a class="btn" href="#" style="top:98px">Click Here</a>
  </section>
</main>

<footer class="newsletter">
  <h2 class="newsletter-title">Newsletter</h2>
  <div class="email-field">Enter Email</div>
  <div class="subscribe">Subscribe</div>
  <div class="social">
    <span role="img" aria-label="Social link"></span>
    <span role="img" aria-label="Social link"></span>
    <span role="img" aria-label="Social link"></span>
  </div>
  <p class="copyright">All Rights Reserved <b>Pelkman Agency</b></p>
</footer>

</body>
</html>
```